Bottled Beer Label Design

See Attached.
Updates
The beer label is printed on transparent pvc sticker, like the Valdermoor label. It meant that the unprinted part will be the color of the bottle. In this case it is amber color.
Attached please find photos of Valdermoor Bottle and label.
Thank you and best of luck.
Target Market(s)
Cater to the age grpoup in the 20's to early 40's in the Pubs and tothe la
Requirements
Must have
- See Attached.
Nice to have
- See Attached.
Should not have
- prefer not to have odd shaped label as the manufacturing will be easy and thus cheaper, and application of the label on to the bottle is less liable to develop defects

```html
<!DOCTYPE html>
<html lang="en">
<head>
<meta charset="utf-8">
<title>Copperfin Brew house – Summer Ale Label</title>
<link rel="stylesheet" href="https://fonts.googleapis.com/css2?family=Bree+Serif&family=Kaushan+Script&family=Italianno&family=Tinos:wght@400;700&display=swap">
<style>
  :root {
    --label-white: #ffffff;
    --ink-black: #060606;
    --brand-red: #e3141c;
    --silver: #a9a9a9;
    --rule-grey: #9a9a9a;
  }
  html, body {
    margin: 0;
    padding: 0;
    width: 1200px;
    height: 1116px;
    overflow: hidden;
    background: var(--label-white);
  }
  .beer-label {
    display: block;
    width: 1200px;
    height: 1116px;
  }
  .label-ground { fill: var(--label-white); }
  .side-band { fill: url(#bandTone); }
  .centre-diamond { fill: var(--brand-red); }
  .title-panel { fill: var(--ink-black); }
  .title-rule { fill: var(--rule-grey); }
  .brand-name {
    font-family: "Bree Serif", serif;
    font-size: 112px;
    fill: var(--brand-red);
  }
  .brand-sub {
    font-family: "Bree Serif", serif;
    font-size: 66px;
    fill: var(--brand-red);
    letter-spacing: 2px;
  }
  .product-name {
    font-family: "Kaushan Script", cursive;
    font-size: 104px;
    fill: var(--silver);
  }
  .arc-tagline {
    font-family: "Italianno", cursive;
    font-size: 66px;
    fill: var(--ink-black);
  }
  .arc-origin {
    font-family: "Bree Serif", serif;
    font-size: 50px;
    fill: var(--silver);
    stroke: var(--ink-black);
    stroke-width: 1.2px;
  }
  .abv-note {
    font-family: "Tinos", serif;
    font-weight: 700;
    font-size: 44px;
    fill: var(--ink-black);
  }
</style>
</head>
<body>
<svg class="beer-label" viewBox="0 0 1200 1116" xmlns="http://www.w3.org/2000/svg">
  <defs>
    <linearGradient id="bandTone" x1="0" y1="0" x2="0" y2="1">
      <stop offset="0" stop-color="#0a0a0a"/>
      <stop offset="0.45" stop-color="#140304"/>
      <stop offset="1" stop-color="#3a0507"/>
    </linearGradient>
    <path id="taglineArc" d="M 165 305 Q 590 -165 965 295"/>
    <path id="originArc" d="M 250 790 Q 540 1360 975 600"/>
  </defs>

  <rect class="label-ground" x="0" y="0" width="1200" height="1116"/>

  <rect class="side-band side-band--left" x="0" y="0" width="168" height="1116"
        role="img" aria-label="Black side band with red swirl and concentric ring ornaments"/>
  <rect class="side-band side-band--right" x="988" y="0" width="212" height="1116"
        role="img" aria-label="Black side band with red swirl and concentric ring ornaments"/>

  <polygon class="centre-diamond" points="599,145 1040,581 599,1023 160,581"/>

  <rect class="title-panel" x="282" y="256" width="590" height="552"/>

  <text class="brand-name" x="577" y="410" text-anchor="middle">Copperfin</text>
  <rect class="title-rule" x="349" y="426" width="494" height="8"/>
  <text class="brand-sub" x="372" y="500">Brew house</text>

  <text class="product-name" x="577" y="700" text-anchor="middle">Summer Ale</text>

  <text class="arc-tagline">
    <textPath href="#taglineArc" startOffset="50%" text-anchor="middle">Handcrafted from the finest ingredients</textPath>
  </text>

  <text class="arc-origin">
    <textPath href="#originArc" startOffset="50%" text-anchor="middle">Proudly brewed &amp; bottled in singapora</textPath>
  </text>

  <text class="abv-note" x="178" y="1102" textLength="330" lengthAdjust="spacingAndGlyphs">5% ALCOHOL</text>
</svg>
</body>
</html>
```